Business Card Design

I do estate sales and would like business card to reflect look and feel of attached logo. I also have copy of logo in .eps and .tif if you need that instead of .jpeg.
Updates

sorry for the delay in reviewing these designs. I will pick one by tomorrow. Here are the absolutes: *must have tagline (we find good homes for your treasures *must use blue and green *must be horizontal *nothing too fancy please submit your best and final. Thanks so much!

Industry/Entity Type

Business

Contact Information for Business Card

Nora Platt

DEALS by NORA
We find good homes for your treasures.

Specializing in one to three-day sales
o (no sale too big or too small)
• Home and garage organizing
• Home Clean-out

Call Nora Platt at 202-555-0187
to schedule.

```html
<!DOCTYPE html>
<html lang="en">
<head>
<meta charset="utf-8">
<title>Deals by Nora – Business Card</title>
<link rel="stylesheet" href="https://fonts.googleapis.com/css2?family=Marcellus&family=Cormorant+Garamond:ital,wght@1,500&display=swap">
<style>
  :root {
    --backdrop: #c4c4c4;
    --card-white: #ffffff;
    --leaf-green: #6e843c;
    --teal: #13829f;
    --ink: #111111;
    --text-light: #ffffff;
  }
  * { box-sizing: border-box; margin: 0; padding: 0; }
  html, body {
    width: 1200px;
    height: 900px;
    overflow: hidden;
    background: var(--backdrop);
  }
  .business-card {
    position: absolute;
    left: 100px;
    top: 165px;
    width: 1000px;
    height: 571px;
    border-radius: 42px;
    overflow: hidden;
    background: var(--card-white);
    font-family: "Marcellus", Georgia, serif;
  }
  .card-shapes {
    position: absolute;
    inset: 0;
    width: 100%;
    height: 100%;
  }
  .brand-name {
    position: absolute;
    left: 48px;
    top: 92px;
    width: 400px;
    color: var(--leaf-green);
    font-weight: 400;
    text-align: center;
    line-height: 1;
  }
  .brand-name .brand-word {
    display: block;
    font-size: 118px;
    letter-spacing: 2px;
  }
  .brand-name .brand-joiner {
    display: block;
    font-size: 62px;
    margin: 4px 0 6px;
  }
  .contact-panel {
    position: absolute;
    left: 620px;
    top: 0;
    width: 350px;
    height: 100%;
    text-align: center;
    color: var(--text-light);
  }
  .owner-name {
    position: absolute;
    top: 62px;
    width: 100%;
    font-size: 36px;
    color: var(--ink);
    font-weight: 400;
  }
  .service-intro {
    position: absolute;
    top: 140px;
    width: 100%;
    font-size: 17px;
    line-height: 28px;
    white-space: nowrap;
  }
  .service-list {
    position: absolute;
    top: 236px;
    width: 100%;
    list-style: none;
    font-size: 21px;
    line-height: 30px;
    white-space: nowrap;
  }
  .service-list li::before { content: "• "; }
  .booking {
    position: absolute;
    top: 372px;
    width: 100%;
    font-size: 22px;
    line-height: 30px;
    color: var(--ink);
  }
  .booking .phone {
    display: block;
    font-size: 34px;
    line-height: 44px;
    color: var(--text-light);
  }
  .slogan-text {
    font-family: "Cormorant Garamond", Georgia, serif;
    font-style: italic;
    font-weight: 500;
    font-size: 28px;
  }
</style>
</head>
<body>
  <section class="business-card" aria-label="Deals by Nora business card">
    <svg class="card-shapes" viewBox="0 0 1000 571" aria-hidden="true">
      <defs>
        <clipPath id="green-field">
          <path d="M610 0 H1000 V571 H432 C560 440 600 250 610 0 Z"/>
        </clipPath>
      </defs>
      <path class="teal-sweep" d="M460 0 C560 120 600 330 432 571 H1000 V0 Z" fill="var(--teal)"/>
      <path class="green-field" d="M610 0 H1000 V571 H432 C560 440 600 250 610 0 Z" fill="var(--leaf-green)"/>
      <path class="divider-line" d="M432 571 C560 440 600 250 610 0" fill="none" stroke="var(--card-white)" stroke-width="7"/>
      <text class="slogan-text" x="70" y="545" textLength="860" lengthAdjust="spacing" fill="var(--leaf-green)">no sale too big or too small</text>
      <text class="slogan-text" x="70" y="545" textLength="860" lengthAdjust="spacing" fill="var(--card-white)" clip-path="url(#green-field)">no sale too big or too small</text>
    </svg>

    <h1 class="brand-name">
      <span class="brand-word">DEALS</span>
      <span class="brand-joiner">by</span>
      <span class="brand-word">NORA</span>
    </h1>

    <div class="contact-panel">
      <h2 class="owner-name">Nora Platt</h2>
      <p class="service-intro">We find good homes for your treasures.<br>Specializing in one to three-day sales</p>
      <ul class="service-list">
        <li>Home and garage organizing</li>
        <li>Home Clean-out</li>
      </ul>
      <p class="booking">Call Nora Platt at<span class="phone">202-555-0187</span>to schedule.</p>
    </div>
  </section>
</body>
</html>
```